Brightmoor Capital Partners- Business Card

We need a professional business card that conveys confidence and trust. Strength. A modern and still yet, traditional financial planner/advisor format. I will upload a logo file or two, you do not have to use it, if it does not work for the design.

Target Market(s)

high net worth

Industry/Entity Type

Finance

Contact Information for Business Card

Address: 24853 Harlow Ave. Suite 610, Huntington Beach, CA 90318, website: brightmoorcapital.example, ph # (555) 276-1948, email address: mpellegrin@brightmoorcapital.example

```html
<!DOCTYPE html>
<html lang="en">
<head>
<meta charset="utf-8">
<title>Brightmoor Capital Partners – Business Card</title>
<link rel="stylesheet" href="https://fonts.googleapis.com/css2?family=Cinzel:wght@500&family=Montserrat:wght@600&family=Roboto:wght@300;400&display=swap">
<style>
  :root {
    --backdrop: #1c1c1e;
    --card: #141414;
    --card-edge: #2a2a2a;
    --gold: #c9a24a;
    --gold-soft: #a88638;
    --ink: #e9e9e9;
    --rule: #6d6d6d;
  }
  * { margin: 0; padding: 0; box-sizing: border-box; }
  html, body {
    width: 1200px; height: 900px; overflow: hidden;
    background: var(--backdrop);
  }
  .canvas {
    position: relative; width: 1200px; height: 900px;
  }
  .card {
    position: absolute; left: 260px; width: 680px; height: 388px;
    background: var(--card);
    border: 1px solid var(--card-edge);
    border-radius: 4px;
    box-shadow: 0 10px 30px rgba(0,0,0,.45);
    overflow: hidden;
  }
  .card--front { top: 40px; }
  .card--back { top: 472px; }

  .brand {
    position: absolute; left: 70px; top: 78px;
    display: flex; align-items: center; gap: 16px;
  }
  .brand__mark {
    width: 30px; height: 30px;
    border: 2px solid var(--gold);
  }
  .brand__name {
    font-family: "Cinzel", serif; font-weight: 500;
    font-size: 27px; letter-spacing: .5px;
    color: var(--gold);
  }

  .holder {
    position: absolute; right: 355px; top: 218px;
    text-align: right;
  }
  .holder__name {
    font-family: "Montserrat", sans-serif; font-weight: 600;
    font-size: 23px; letter-spacing: .5px;
    color: var(--gold);
    text-transform: uppercase;
  }
  .holder__title {
    margin-top: 6px;
    font-family: "Roboto", sans-serif; font-weight: 400;
    font-size: 17px; color: var(--ink);
  }

  .divider {
    position: absolute; left: 350px; top: 160px;
    width: 1px; height: 180px; background: var(--rule);
  }

  .contact {
    position: absolute; left: 374px; top: 166px;
    font-family: "Roboto", sans-serif; font-weight: 300;
    font-size: 14.5px; line-height: 1.5; color: var(--ink);
    list-style: none;
  }
  .contact__address { margin-bottom: 12px; }
  .contact__line { display: flex; align-items: center; gap: 9px; }
  .contact__icon { width: 14px; height: 14px; flex: none; }

  .pattern-field {
    position: absolute; inset: 0;
    background: radial-gradient(ellipse at 35% 40%, #2b2b2d 0%, #161616 60%, #0d0d0d 100%);
  }
</style>
</head>
<body>
<main class="canvas">

  <section class="card card--front" aria-label="Business card front">
    <div class="brand">
      <span class="brand__mark"></span>
      <span class="brand__name">Brightmoor Capital Partners</span>
    </div>

    <div class="holder">
      <p class="holder__name">Marcus L. Pellegrin</p>
      <p class="holder__title">Founder &amp; CEO</p>
    </div>

    <div class="divider"></div>

    <ul class="contact">
      <li class="contact__address">24853 Harlow Ave.<br>Suite 610 Huntington Beach, CA 90318</li>
      <li class="contact__line">
        <svg class="contact__icon" viewBox="0 0 16 16" aria-hidden="true"><path fill="#c9a24a" d="M3.6 1.5l2.2 2.6-1.3 1.6c.9 2 2.7 3.8 4.8 4.8l1.6-1.3 2.6 2.2-1.4 2.1C6.5 13.4 2.6 9.5 1.5 3z"/></svg>
        (555) 276-1948
      </li>
      <li class="contact__line">
        <svg class="contact__icon" viewBox="0 0 16 16" aria-hidden="true"><rect x="1.5" y="3.5" width="13" height="9" fill="#c9a24a"/><path d="M1.5 3.5L8 9l6.5-5.5" fill="none" stroke="#141414" stroke-width="1.3"/></svg>
        mpellegrin@brightmoorcapital.example
      </li>
      <li class="contact__line">
        <svg class="contact__icon" viewBox="0 0 16 16" aria-hidden="true"><circle cx="8" cy="8" r="6.5" fill="#c9a24a"/><path d="M1.5 8h13M8 1.5c-2.4 2.6-2.4 10.4 0 13M8 1.5c2.4 2.6 2.4 10.4 0 13" fill="none" stroke="#141414" stroke-width="1"/></svg>
        www.brightmoorcapital.example
      </li>
    </ul>
  </section>

  <section class="card card--back" aria-label="Business card back">
    <div class="pattern-field" role="img" aria-label="Repeating embossed emblem pattern in black with a single gold emblem accent"></div>
  </section>

</main>
</body>
</html>
```